Painting Contractor Business Card Design

We are looking for a cool, bold, modern, polished, business card design. We are a high-end residential painting contractor. Please incorporate our logo and keep with our green/black color scheme. We are interested in seeing 2-sided and 1-sided options. Thank you very much!

Industry/Entity Type

Business

Contact Information for Business Card

Info for the card:
Owen Talsky
mobile 206-555-0193
email owen@kestrowfinish.net
web www.kestrowfinish.net

```html
<!DOCTYPE html>
<html lang="en">
<head>
<meta charset="utf-8">
<title>Kestrow Finish – Business Card</title>
<link rel="stylesheet" href="https://fonts.googleapis.com/css2?family=Raleway:wght@300;600&family=Lato:wght@400&display=swap">
<style>
  :root {
    --bg-top: #2a2a2a;
    --bg-bottom: #050505;
    --brand-green: #3dab4a;
    --card-paper: #ebe8e7;
    --ink: #1d1d1d;
    --ink-soft: #6a6a6a;
    --white: #ffffff;
  }
  * { box-sizing: border-box; margin: 0; padding: 0; }
  html, body { width: 1200px; height: 900px; overflow: hidden; }
  body {
    position: relative;
    background: linear-gradient(180deg, var(--bg-top) 0%, var(--bg-bottom) 100%);
    font-family: "Lato", Arial, sans-serif;
  }
  .card { position: absolute; width: 259px; height: 441px; overflow: hidden; }

  /* Front */
  .card-front { left: 343px; top: 206px; background: var(--card-paper); }
  .front-side-bar { position: absolute; left: 0; top: 0; width: 28px; height: 244px; background: var(--brand-green); }
  .front-corner-block { position: absolute; right: 0; bottom: 0; width: 28px; height: 65px; background: var(--brand-green); }
  .brand-lockup {
    position: absolute; left: 80px; top: 34px; width: 118px;
    display: flex; flex-direction: column; align-items: center; gap: 10px;
  }
  .brand-square { width: 38px; height: 38px; background: var(--brand-green); }
  .brand-name {
    font-family: "Raleway", Arial, sans-serif; font-weight: 600;
    font-size: 19px; line-height: 1.15; letter-spacing: 1px;
    color: var(--brand-green); text-align: center; text-transform: uppercase;
  }
  .name-band {
    position: absolute; left: 87px; top: 163px; width: 172px; height: 32px;
    background: var(--brand-green); color: var(--white);
    font-family: "Raleway", Arial, sans-serif; font-weight: 300;
    font-size: 20px; line-height: 32px; text-align: center; letter-spacing: 0.5px;
  }
  .job-title {
    position: absolute; left: 87px; top: 200px; width: 162px;
    font-size: 12px; color: var(--ink); text-align: center;
  }
  .address {
    position: absolute; left: 30px; top: 256px; width: 196px;
    font-size: 13px; line-height: 14px; color: var(--ink); text-align: center;
  }
  .contact-list { position: absolute; left: 58px; top: 301px; list-style: none; }
  .contact-list li {
    display: flex; align-items: center; gap: 8px;
    height: 17.3px; font-size: 13px; color: var(--ink-soft);
  }
  .contact-icon { width: 10px; height: 10px; fill: var(--brand-green); flex: none; }

  /* Back */
  .card-back { left: 667px; top: 203px; height: 443px; background: var(--brand-green); }
  .back-wordmark {
    position: absolute; left: 98px; top: 64px; height: 250px;
    writing-mode: vertical-rl; transform: rotate(180deg);
    font-family: "Raleway", Arial, sans-serif; font-weight: 600;
    font-size: 27px; letter-spacing: 1.5px; color: var(--white);
    text-transform: uppercase; white-space: nowrap; text-align: center;
  }
  .back-square { position: absolute; left: 100px; top: 336px; width: 36px; height: 36px; background: var(--white); }
</style>
</head>
<body>

<section class="card card-front" aria-label="Business card front">
  <div class="front-side-bar"></div>
  <div class="brand-lockup">
    <div class="brand-square"></div>
    <div class="brand-name">Kestrow<br>Finish</div>
  </div>
  <div class="name-band">OWEN TALSKY</div>
  <div class="job-title">Managing Director</div>
  <p class="address">1234, Address Goes Here<br>Country Name, 123456</p>
  <ul class="contact-list">
    <li><svg class="contact-icon" viewBox="0 0 10 10"><path d="M3 0h4a1 1 0 0 1 1 1v8a1 1 0 0 1-1 1H3a1 1 0 0 1-1-1V1a1 1 0 0 1 1-1zm0 1.5v6h4v-6z"/></svg>206-555-0193</li>
    <li><svg class="contact-icon" viewBox="0 0 10 10"><path d="M0 3c0-2 10-2 10 0v1.5H7.5V3.3h-5v1.2H0zM2 5h6l1.5 4h-9z"/></svg>206-555-0193</li>
    <li><svg class="contact-icon" viewBox="0 0 10 10"><path d="M2.5 0h5v3h-5zM0 3.5h10v4.5H8V10H2V8H0zm3 3V9h4V6.5z"/></svg>206-555-0193</li>
    <li><svg class="contact-icon" viewBox="0 0 10 10"><path d="M0 2h10v6H0zm1 1v.3l4 2.6 4-2.6V3z"/></svg>owen@kestrowfinish.net</li>
    <li><svg class="contact-icon" viewBox="0 0 10 10"><path d="M4 6 6 4M3.5 4.5 2 6a1.4 1.4 0 0 0 2 2l1.5-1.5M6.5 5.5 8 4a1.4 1.4 0 0 0-2-2L4.5 3.5" fill="none" stroke="#3dab4a" stroke-width="1.4" stroke-linecap="round"/></svg>www.kestrowfinish.net</li>
  </ul>
  <div class="front-corner-block"></div>
</section>

<section class="card card-back" aria-label="Business card back">
  <div class="back-wordmark">Kestrow Finish</div>
  <div class="back-square"></div>
</section>

</body>
</html>
```